R&T Cleanwave Stripping Business Card

We are in need of a business card design for our new Texas based company called 'R&T Cleanwave Stripping'. Our new innovative mobile media blasting service utilizes recycled material and a new water based process that eliminates all dust (i.e. as apposed to the old sand blasting format). Our 'advanced surface preparation' service targets multiple industries such as automotive, Industrial, marine and structural (graffiti removal). We would like to see the design include a recycling type logo or concept that utilizes colors such as black, various shades of green, some white, yellow and/or grey (e.g. perhaps a blackish background). The final design should look simple and professional and should clearly communicate the environmentally friendly approach through logo or design (i.e. Eco-Friendly, Go Green or Blast Green methodologies). Thank you in advance!
Updates

Please pardon any inconvenience. We have decided to pursue a two sided business card. All original information/designs requirements remains the same for the front. However, we would like back of the card to state the following: "We bring the power of Hydroveil Media Scouring equipment to your location. We can remove any coating from any surface. Bullets include: Paint Stripping, Auto Restoration, Graffiti Removal, Black Walls & Stone, Concrete, Boats, Iron Fences, Tractors & Trailers, Pools & Fountains, Wood Restoration.

Industry/Entity Type

Recycling

Contact Information for Business Card

R&T Cleanwave Stripping, LLC - Gordon Pelly, MBA, PMP - cell: 915-382-6091, office: 915-627-8853 - gpelly@rtcleanwavestripping.com - CEO/Founder

Requirements
Must have
• Recycle or environmentally friendly logos or design.
Nice to have
• Business oriented design with an aggressive look. Also, if possible would like to see R&T incorporated into the design or logo. Please note that we have decided to add the option of adding details to the back of the card (2 sided). The front should contain the logo/design and the back should have the following details listed: "We bring the power of Hydroveil Media Scouring equipment to your location. We can remove any coating from any surface. Bullets include: Paint Stripping, Auto Restoration, Graffiti Removal, Black Walls & Stone, Concrete, Boats, Iron Fences, Tractors & Trailers, Pools & Fountains, Wood Restoration.

```html
<!DOCTYPE html>
<html lang="en">
<head>
<meta charset="utf-8">
<title>R&amp;T Cleanwave Stripping – Business Card</title>
<link rel="stylesheet" href="https://fonts.googleapis.com/css2?family=Lato:wght@400;700;900&display=swap">
<style>
  :root {
    --canvas: #e9e7e3;
    --ink: #121614;
    --ink-soft: #1c2320;
    --paper: #ffffff;
    --green: #8fd14f;
    --green-deep: #6fae34;
    --grey: #6b6e6c;
    --grey-light: #b9bcba;
  }
  * { box-sizing: border-box; margin: 0; padding: 0; }
  html, body { width: 1200px; height: 800px; overflow: hidden; }
  body {
    background: var(--canvas);
    font-family: "Lato", Arial, sans-serif;
    display: flex;
    align-items: center;
    justify-content: center;
    gap: 40px;
  }
  .card {
    position: relative;
    width: 540px;
    height: 309px;
    overflow: hidden;
    box-shadow: 0 10px 28px rgba(0,0,0,.18);
  }

  /* Front */
  .card--front { background: var(--paper); }
  .front__art { position: absolute; inset: 0; }
  .brand { position: absolute; left: 34px; top: 28px; display: flex; align-items: center; gap: 14px; }
  .brand__square { width: 46px; height: 46px; background: var(--green); }
  .brand__text { color: var(--ink); }
  .brand__initials { font-size: 38px; font-weight: 700; letter-spacing: 3px; line-height: 1; }
  .brand__name { font-size: 21px; font-weight: 400; color: #3a3d3b; margin-top: 2px; }
  .holder { position: absolute; left: 34px; top: 112px; }
  .holder__name { color: var(--green); font-weight: 900; font-size: 17px; letter-spacing: .5px; text-transform: uppercase; }
  .holder__role { color: var(--grey); font-size: 11px; margin-top: 3px; }
  .contact { position: absolute; left: 24px; top: 186px; list-style: none; color: var(--paper); font-size: 12.5px; }
  .contact li { display: flex; align-items: center; gap: 8px; margin-bottom: 5px; }
  .contact svg { width: 14px; height: 14px; flex: none; }

  /* Back */
  .card--back { background: linear-gradient(135deg, var(--ink-soft), var(--ink) 70%); color: var(--paper); }
  .back__brand { position: absolute; left: 30px; top: 28px; color: var(--grey-light); }
  .back__initials { font-size: 26px; font-weight: 700; letter-spacing: 3px; }
  .back__name { font-size: 13px; margin-top: 2px; }
  .statement { position: absolute; left: 30px; right: 30px; top: 100px; color: var(--green); font-size: 12.5px; font-weight: 700; line-height: 1.45; }
  .services {
    position: absolute; left: 30px; right: 30px; top: 160px;
    list-style: none; columns: 2; column-gap: 30px;
    font-size: 12.5px; color: #d6d8d6;
  }
  .services li { display: flex; justify-content: flex-end; align-items: center; gap: 10px; margin-bottom: 5px; }
  .services li::after {
    content: ""; width: 0; height: 0;
    border-left: 5px solid transparent; border-right: 5px solid transparent;
    border-bottom: 8px solid var(--green);
  }
</style>
</head>
<body>

<section class="card card--front" aria-label="Business card front">
  <svg class="front__art" viewBox="0 0 540 309" preserveAspectRatio="none" aria-hidden="true">
    <polygon points="0,168 540,168 540,309 0,309" fill="#121614"/>
    <polygon points="0,160 540,160 540,166 0,166" fill="#8fd14f"/>
    <polygon points="300,309 360,230 392,230 332,309" fill="#8fd14f"/>
    <polygon points="360,309 420,230 540,230 540,309" fill="#8fd14f"/>
    <polygon points="410,309 470,244 540,244 540,309" fill="#121614"/>
  </svg>

  <div class="brand">
    <span class="brand__square" aria-hidden="true"></span>
    <div class="brand__text">
      <div class="brand__initials">R&amp;T</div>
      <div class="brand__name">Cleanwave Stripping, LLC</div>
    </div>
  </div>

  <div class="holder">
    <p class="holder__name">Gordon Pelly, MBA, PMP</p>
    <p class="holder__role">CEO | Founder</p>
  </div>

  <ul class="contact">
    <li>
      <svg viewBox="0 0 14 14" aria-hidden="true"><circle cx="7" cy="7" r="7" fill="#8fd14f"/><path d="M4.6 3.6l1.3 1.6-.7.9c.5 1.1 1.3 1.9 2.4 2.4l.9-.7 1.6 1.3-.6 1.2C6.6 10.2 3.8 7.4 3.4 4.2z" fill="#121614"/></svg>
      915-382-6091
    </li>
    <li>
      <svg viewBox="0 0 14 14" aria-hidden="true"><circle cx="7" cy="7" r="7" fill="#8fd14f"/><rect x="4.5" y="3" width="5" height="8" rx="1" fill="#121614"/></svg>
      915-627-8853
    </li>
    <li>
      <svg viewBox="0 0 14 14" aria-hidden="true"><circle cx="7" cy="7" r="7" fill="#8fd14f"/><rect x="3.5" y="4.5" width="7" height="5" fill="#121614"/><path d="M3.5 4.5L7 7.3l3.5-2.8" stroke="#8fd14f" stroke-width=".8" fill="none"/></svg>
      gpelly@rtcleanwavestripping.com
    </li>
  </ul>
</section>

<section class="card card--back" aria-label="Business card back">
  <div class="back__brand">
    <div class="back__initials">R&amp;T</div>
    <div class="back__name">Cleanwave Stripping, LLC</div>
  </div>

  <p class="statement">
    We bring the power of Hydroveil Media Scouring equipment to your location.<br>
    We can remove any coating from any surface.
  </p>

  <ul class="services">
    <li>Paint Stripping</li>
    <li>Auto Restoration</li>
    <li>Graffiti Removal</li>
    <li>Black Walls &amp; Stone</li>
    <li>Concrete</li>
    <li>Boats</li>
    <li>Iron Fences</li>
    <li>Tractors &amp; Trailers</li>
    <li>Pools &amp; Fountains</li>
    <li>Wood Restoration</li>
  </ul>
</section>

</body>
</html>
```